Maple Brook Concrete business card design

We need a business card developed for a local ready mix concrete company. We want a 2 sided design

The front just needs the basic contact info:

Raymond Vasquelli
P.555-014-2261
F. 555-014-2287
www.MapleBrookConcrete.Com
Raymond@MapleBrookConcrete.com
P.O Box 614
Cedar Glen, NJ, 07192

Service All of North And Central New Jersey With Ready Mix Concrete

The back will have a simple bullet point list:
• Metered Delivery - Use only what you pay for
• No Waste
• Multiple slumps on the fly
• No minimum delivery
• 24-7 service, all year
• No Hot Loads
• Fastest Service in the industry
Updates

I like the submissions using the existing colors. I think blue might also be a color to use as well. For the next trucks we order we will probably paint them blue. Colbalt blue

I must have made a typo: It should read, Serving all of North and Central New Jersey. It should also say: Pay for only what you use.

Target Market(s)

We will be targeting the construction industry

Industry/Entity Type

Concrete

Font styles to use
Serif
Sans Serif

Colors
ec2027

Requirements
Must have
• It needs to have a clean uncluttered look. The back is dedicated to telling customer what we do. Our advantage is we use a truck that delivers concrete with several advantages over barrel trucks, hence, why the back bullet points are important
Nice to have
• Our logo. I think since our logo is green, the front might look good with some red, like a red background (also the color of our truck)
Should not have
• clip art.

```html
<!DOCTYPE html>
<html lang="en">
<head>
<meta charset="utf-8">
<title>Maple Brook Concrete – Business Card</title>
<link href="https://fonts.googleapis.com/css2?family=Michroma&display=swap" rel="stylesheet">
<style>
  :root {
    --stage: #e4e4e2;
    --card: #ffffff;
    --card-shade: #ececec;
    --brand-green: #7cc242;
    --band-grey: #9b9b9b;
    --ink: #4a4a4a;
    --ink-soft: #6d6d6d;
    --icon: #3d3d3d;
  }
  * { box-sizing: border-box; margin: 0; padding: 0; }
  html, body { width: 1200px; height: 901px; overflow: hidden; }
  body {
    background: var(--stage);
    font-family: "Michroma", "Arial", sans-serif;
    color: var(--ink);
    display: flex;
    align-items: center;
    justify-content: center;
    gap: 44px;
  }
  .card {
    position: relative;
    width: 530px;
    height: 304px;
    border-radius: 30px;
    background: radial-gradient(ellipse at 55% 35%, var(--card) 40%, var(--card-shade) 100%);
    box-shadow: 0 6px 18px rgba(0,0,0,.16);
    overflow: hidden;
  }
  .card__swoosh { position: absolute; inset: 0; width: 100%; height: 100%; }
  .card__web {
    position: absolute;
    left: 58px;
    bottom: 22px;
    font-size: 11px;
    letter-spacing: 1.2px;
    color: #fff;
  }
  .brand-name {
    position: absolute;
    color: var(--brand-green);
    font-size: 25px;
    line-height: 1.15;
    text-transform: uppercase;
    text-align: center;
    letter-spacing: 1px;
    white-space: nowrap;
  }
  .card--front .brand-name { top: 28px; left: 170px; width: 330px; }
  .card--back .brand-name { top: 24px; left: 0; width: 530px; font-size: 22px; }

  .contact {
    position: absolute;
    top: 112px;
    left: 30px;
    display: flex;
    gap: 14px;
  }
  .contact__person {
    text-align: right;
    font-size: 8px;
    letter-spacing: .8px;
    color: var(--ink-soft);
    line-height: 1.7;
    padding-top: 2px;
    white-space: nowrap;
  }
  .contact__name { font-size: 10px; color: var(--ink); letter-spacing: 1px; }
  .contact__role { margin-bottom: 10px; }
  .contact__divider { width: 1px; background: var(--ink-soft); align-self: stretch; }
  .contact__lines { list-style: none; font-size: 8.5px; letter-spacing: .6px; color: var(--ink); white-space: nowrap; }
  .contact__lines li { display: flex; align-items: center; gap: 7px; height: 17px; }
  .contact__lines svg { width: 11px; height: 11px; flex: none; }

  .advantages {
    position: absolute;
    top: 92px;
    left: 0;
    width: 530px;
    display: flex;
    justify-content: center;
  }
  .advantages__list {
    list-style: none;
    font-size: 8.5px;
    letter-spacing: .6px;
    line-height: 15px;
    color: var(--ink);
    white-space: nowrap;
  }
  .advantages__list li { display: flex; align-items: center; gap: 8px; }
  .advantages__list li::before {
    content: "";
    width: 5px; height: 5px;
    border-radius: 50%;
    background: var(--brand-green);
    flex: none;
  }
</style>
</head>
<body>

  <section class="card card--front" aria-label="Card front">
    <svg class="card__swoosh" viewBox="0 0 530 304" preserveAspectRatio="none" aria-hidden="true">
      <path d="M0 200 C 150 262, 360 272, 530 286 L530 304 L0 304 Z" fill="var(--band-grey)"/>
      <path d="M0 212 C 150 270, 360 280, 530 292 L530 304 L0 304 Z" fill="var(--brand-green)"/>
    </svg>
    <div class="brand-name">Maple Brook<br>Concrete</div>

    <div class="contact">
      <div class="contact__person">
        <div class="contact__name">RAYMOND VASQUELLI</div>
        <div class="contact__role">Owner / C.E.O</div>
        <div>P.O Box 614</div>
        <div>Cedar Glen, NJ, 07192</div>
      </div>
      <div class="contact__divider"></div>
      <ul class="contact__lines">
        <li><svg viewBox="0 0 12 12"><circle cx="6" cy="6" r="6" fill="var(--icon)"/><path d="M4 3.2h1.2l.6 1.6-.8.6a4 4 0 0 0 1.6 1.6l.6-.8 1.6.6V8a.8.8 0 0 1-.8.8A4.8 4.8 0 0 1 3.2 4 .8.8 0 0 1 4 3.2z" fill="#fff"/></svg>P. 555-014-2261</li>
        <li><svg viewBox="0 0 12 12"><circle cx="6" cy="6" r="6" fill="var(--icon)"/><rect x="3" y="5" width="6" height="3.5" fill="#fff"/><rect x="4" y="3" width="4" height="2" fill="#fff"/></svg>F. 555-014-2287</li>
        <li><svg viewBox="0 0 12 12"><circle cx="6" cy="6" r="6" fill="var(--icon)"/><rect x="3" y="3.8" width="6" height="4.4" fill="#fff"/><path d="M3 3.8l3 2.4 3-2.4" stroke="var(--icon)" stroke-width=".7" fill="none"/></svg>Raymond@MapleBrookConcrete.com</li>
        <li><svg viewBox="0 0 12 12"><circle cx="6" cy="6" r="6" fill="var(--icon)"/><circle cx="6" cy="6" r="3" fill="none" stroke="#fff" stroke-width=".8"/><path d="M3 6h6M6 3v6" stroke="#fff" stroke-width=".7"/></svg>www.MapleBrookConcrete.Com</li>
      </ul>
    </div>

    <div class="card__web">www.MapleBrookConcrete.Com</div>
  </section>

  <section class="card card--back" aria-label="Card back">
    <svg class="card__swoosh" viewBox="0 0 530 304" preserveAspectRatio="none" aria-hidden="true">
      <path d="M0 222 C 150 272, 360 278, 530 288 L530 304 L0 304 Z" fill="var(--band-grey)"/>
      <path d="M0 232 C 150 278, 360 284, 530 294 L530 304 L0 304 Z" fill="var(--brand-green)"/>
    </svg>
    <div class="brand-name">Maple Brook<br>Concrete</div>
    <div class="advantages">
      <ul class="advantages__list">
        <li>Metered Delivery – Pay for only what you use</li>
        <li>No Waste</li>
        <li>Multiple slumps on the fly</li>
        <li>No minimum delivery</li>
        <li>24-7 service, all year</li>
        <li>No Hot Loads</li>
        <li>Fastest Service in the industry</li>
      </ul>
    </div>
  </section>

</body>
</html>
```